Business Card & Logo Design Project

I am looking for a slick/simple design for a logo and business card, for a music Producer/Mixer/Engineer.

I'm based in Tokyo, Japan and I help my clients polish up their creation to major radio/TV status. My clients pay me for my taste, sense of balance expertise and creative direction/

Design should give impression of seal of quality, professionalism, and enthusiasm need some sort of a logo like design for "vantrix productions".

Please don't include music notes or instruments or anything musically related and anything samurai or ninja or too much Japan in them on the design.

I like clever, slick stuff that's not too obvious.
I also like a smooth gradation type transition. My favorite color is deep dark blue/

Good Luck and Thank you for your effort.
Updates

I would like a two-sided design for this one.
One side with "vantrix productions" (all lower case) on, and the other side with my name and contact info.

Please also consider portrait position (or direction).  (as opposed to landscape) 

Target Market(s)

My primary targets are artists & bands, who want absolute best for their creation.

Industry/Entity Type

Business

Requirements
Must have
• Two-Sided
1, vantrix productions
2, Kenji Harumoto, Producer/Mixer/Engineer, +81 090 4827 3516, brambleway@mailnest.example
Nice to have
• Any suggestions are welcome//
Should not have
• Anything music related images.
(e.g. CD, music notations, instruments etc.)

```html
<!DOCTYPE html>
<html lang="en">
<head>
<meta charset="utf-8">
<title>vantrix productions – business cards</title>
<link rel="stylesheet" href="https://fonts.googleapis.com/css2?family=Tinos:wght@400;700&display=swap">
<style>
  :root {
    --navy: #2e3a94;
    --sky: #5bc8ee;
    --ink: #161616;
    --paper: #ffffff;
    --paper-soft: #f6f7f5;
    --edge: #1f2a6e;
    --edge-dark: #222;
    --eq-green: #dfe8b0;
    --eq-grey: #cfcfcf;
  }
  * { box-sizing: border-box; margin: 0; padding: 0; }
  html, body { width: 1200px; height: 935px; overflow: hidden; background: var(--paper); }
  body { position: relative; font-family: "Tinos", "Times New Roman", serif; }

  .card {
    position: absolute;
    width: 572px;
    height: 362px;
    border-radius: 26px;
    overflow: hidden;
    background: var(--paper);
  }
  .card--brand-blue   { left: 5px;   top: 5px;   border: 2px solid var(--edge); }
  .card--contact-blue { left: 605px; top: 5px;   border: 2px solid var(--edge); }
  .card--brand-eq     { left: 33px;  top: 564px; border: 2px solid var(--edge-dark); }
  .card--contact-eq   { left: 623px; top: 564px; border: 2px solid var(--edge-dark); background: var(--paper-soft); }

  .blue-field {
    position: absolute; inset: 0;
    background: linear-gradient(115deg, var(--paper) 0%, var(--paper) 58%, var(--sky) 80%, var(--navy) 100%);
  }

  .wordmark {
    position: absolute;
    display: flex;
    align-items: center;
    gap: 10px;
    font-weight: 700;
    white-space: nowrap;
  }
  .wordmark__dot { border-radius: 50%; flex: none; }

  .card--brand-blue .wordmark { left: 28px; top: 160px; font-size: 38px; color: var(--navy); }
  .card--brand-blue .wordmark__dot { width: 32px; height: 32px; background: var(--navy); }

  .contact { position: absolute; left: 18px; top: 8px; }
  .contact__name { font-size: 40px; font-weight: 400; line-height: 1.1; }
  .contact__role { font-size: 24px; font-weight: 700; margin-top: 6px; }
  .contact__line { font-size: 24px; }
  .contact__phone { margin-top: 40px; }
  .contact__email { margin-top: 44px; }

  .card--contact-blue .contact { color: var(--navy); }
  .card--contact-eq .contact { color: var(--ink); }

  .wordmark--small { right: 20px; bottom: 22px; font-size: 20px; gap: 6px; }
  .card--contact-blue .wordmark--small { color: var(--paper); }
  .card--contact-blue .wordmark__dot { width: 16px; height: 16px; background: var(--paper); }
  .card--contact-eq .wordmark--small { color: var(--ink); }
  .card--contact-eq .wordmark__dot { width: 16px; height: 16px; background: var(--ink); }

  .eq-field {
    position: absolute; inset: 0;
    background: linear-gradient(180deg, #eef2e4 0%, var(--eq-green) 45%, var(--eq-grey) 100%);
  }
  .card--brand-eq .wordmark {
    left: 0; right: 0; top: 160px;
    justify-content: center;
    font-size: 50px;
    color: var(--ink);
  }
</style>
</head>
<body>

  <section class="card card--brand-blue" aria-label="Brand side, blue">
    <div class="blue-field" role="img" aria-label="Decorative blue sweep from white into light blue and deep navy"></div>
    <div class="wordmark"><span class="wordmark__dot"></span>vantrix productions</div>
  </section>

  <section class="card card--contact-blue" aria-label="Contact side, blue">
    <div class="blue-field" role="img" aria-label="Decorative blue sweep from white into light blue and deep navy"></div>
    <div class="contact">
      <h1 class="contact__name">Kenji Harumoto</h1>
      <p class="contact__role">Producer | Mixer | Engineer</p>
      <p class="contact__line contact__phone">(+81) 090 4827 3516</p>
      <p class="contact__line contact__email">brambleway@mailnest.example</p>
    </div>
    <div class="wordmark wordmark--small"><span class="wordmark__dot"></span>vantrix productions</div>
  </section>

  <section class="card card--brand-eq" aria-label="Brand side, level meter">
    <div class="eq-field" role="img" aria-label="Pattern of green and grey rounded level-meter blocks"></div>
    <div class="wordmark">vantrix productions</div>
  </section>

  <section class="card card--contact-eq" aria-label="Contact side, plain">
    <div class="contact">
      <h2 class="contact__name">Kenji Harumoto</h2>
      <p class="contact__role">Producer | Mixer | Engineer</p>
      <p class="contact__line contact__phone">(+81) 090 4827 3516</p>
      <p class="contact__line contact__email">brambleway@mailnest.example</p>
    </div>
    <div class="wordmark wordmark--small"><span class="wordmark__dot"></span>vantrix productions</div>
  </section>

</body>
</html>
```